Can you design the next best-selling "bumper sticker"?

The business concept is to produce new versions of the traditional "baby on board"-sticker.
Part of the concept is using magnet technology in stead of stickers, allowing the customers to swap designs easily. We are now seeking to expant our sortiment of designs.
We want combinations of text and design elements, with a modern expression. For inspiration, you may take a look at this web page selling baby design: http://www.pumlebo.no/collections/varde-hjem , as they use much of the same color pallet that we like, and also cute modern design elements.
Make it innovative, make it funny, or just seriously cute!
Since our business is located in Norway, we need the text to be in norwegian. Text options are as following:
1. "Baby om bord" (translation: baby on board)
2. "Baby om bord - Hold avstand" (translation: baby on board - keep your distance)
3. "Baby om bord - Kjør forsiktig" (translation: baby on board - drive carefully)
4. "Småfolk ombord" (translation: little people on board)
5. "Småfolk ombord - Hold avstand" (translation: little people on board - keep your distance)
6. "Søt og trivelig baby om bord" (translation: cute and nice baby on board)
7. "Søt og trivelig baby om bord - Hold avstand" (translation: cute and nice baby on board - keep your distance)
The design should have a rectangular shape, not a diamond shape.
Young parents who own a car
Baby

```html
<!DOCTYPE html>
<html lang="no">
<head>
<meta charset="utf-8">
<title>Søt og trivelig baby om bord – Hold avstand</title>
<link rel="stylesheet" href="https://fonts.googleapis.com/css2?family=Fredoka:wght@700&display=swap">
<style>
  :root {
    --page-bg: #ffffff;
    --magnet-cyan: #8ff4f2;
    --outline-white: #ffffff;
  }
  html, body {
    margin: 0;
    padding: 0;
    width: 1200px;
    height: 900px;
    overflow: hidden;
    background: var(--page-bg);
  }
  .canvas {
    display: block;
    width: 1200px;
    height: 900px;
  }
  .magnet-plate {
    fill: var(--magnet-cyan);
  }
  .footprints-area {
    fill: var(--outline-white);
    opacity: 0.55;
  }
  .slogan {
    font-family: "Fredoka", "Arial Rounded MT Bold", sans-serif;
    font-weight: 700;
    fill: var(--magnet-cyan);
    stroke: var(--outline-white);
    stroke-linejoin: round;
    paint-order: stroke fill;
  }
  .slogan-small {
    font-size: 34px;
    stroke-width: 8px;
  }
  .slogan-large {
    font-size: 62px;
    stroke-width: 11px;
  }
  .slogan-warning {
    font-size: 44px;
    stroke-width: 9px;
  }
</style>
</head>
<body>
<svg class="canvas" viewBox="0 0 1200 900" xmlns="http://www.w3.org/2000/svg">
  <rect class="magnet-plate" x="317" y="308" width="567" height="284"/>

  <path class="footprints-area" role="img" aria-label="Two white baby footprints with round toes"
        d="M350 440 C350 400 380 390 410 400 C430 360 470 350 520 355 C575 360 592 420 590 480
           C588 505 570 510 545 505 C520 530 480 545 430 538 C385 532 350 500 350 440 Z"/>

  <text class="slogan slogan-small" x="710" y="356" textLength="124" lengthAdjust="spacingAndGlyphs">Søt og</text>
  <text class="slogan slogan-small" x="693" y="401" textLength="141" lengthAdjust="spacingAndGlyphs">trivelig</text>
  <text class="slogan slogan-small" x="672" y="446" textLength="162" lengthAdjust="spacingAndGlyphs">baby om</text>
  <text class="slogan slogan-large" x="680" y="507" textLength="154" lengthAdjust="spacingAndGlyphs">bord</text>
  <text class="slogan slogan-warning" x="518" y="568" textLength="318" lengthAdjust="spacingAndGlyphs">Hold avstand</text>
</svg>
</body>
</html>
```